IRON SASH VIGOUR CERTIFICATE

Corvane Kickfist Inc is wanting to introduce a fitness system based upon certificates reflecting rank; White - Yellow - Blue - Red - Black.

The Certificate "MUST" have on it "IRON SASH VIGOUR"

The Certificate "MUST" have a martial arts theme!

The Certificate "MUST" reflect the fitness requirements for each rank.

The colour scheme for each Certificate "MUST" reflect the belt rank

The Certificate must include at least one martial arts graphic / motif

The certificate must have the Corvane KKF LOGO

We will need a certificate template that can be for all levels but reflect the rank and fitness level. The certificate can be either traditional or modern style but must reflect a martial art themes. The certificate must have the Corvane Kickfist logo incorporated into the certificate with signature space for senior instructors Gus Pelham & Nessa Crail-Pelham. The certificates should be eye catching and exciting to look at. It should bold and incorporate martial art motifs etc The fitness requirements are not onerous and the certificate system is created to incentivise physical activity and correct technique rather than creating an impossible standards only Olympians can achieve. The majority of our students are upper primary and lower secondary from 11yr-15yrs. Certificate should be youthful but not silly. The certificate template will be reproduced for each colour belt.White = 10 push ups 10 Sit ups 10 squats 10 Jumping Jacks 20 sec plank 400m continuous run Demonstrate beginner stretching techniqueYellow = 20 push ups 20 sit ups 20 squats 20 Jumping Jacks 40 Sec plank 800m continuous run Demonstrate intermediate stretching techniqueBlue = 30 push ups 30 sit ups 30 squats 30 Jumping Jacks 60 Sec plank 1200m continuous run Demonstrate intermediate stretching techniqueRed = 40 push ups 40 sit ups 40 squats 40 Jumping Jacks 75sec plank 1600m run Demonstrate advanced stretching techniqueBlack = 50 push ups 50 sit ups 50 squats 50 Jumping jacks 90 sec planks 2000m continuous run Demonstrate advanced stretching technique
Updates

HI Designers, Please go for modern and professionals. Several designs have used traditional motifs of water dragons or lattice bordering. This looks old school. Please do not use martial art silhouettes as it looks amateur. Definately looking for upmarket high quality presentations.

Logo Text

IRON SASH VIGOUR

Font styles to use
Decorative

Colors

Designer to choose colors to be used in the design.

Requirements
Must have
• This will be a template foe all coloured ranks of fitness, Be bold, memorable, should be themed to martial arts etc

```html
<!DOCTYPE html>
<html lang="en">
<head>
<meta charset="utf-8">
<title>Iron Sash Vigour – White Belt Certificate</title>
<link rel="stylesheet" href="https://fonts.googleapis.com/css2?family=Cinzel:wght@400;600;700&family=Cormorant+Garamond:wght@600&family=Great+Vibes&family=Source+Sans+3:wght@400;600&display=swap">
<style>
  :root {
    --backdrop: #3a3a3c;
    --paper: #ffffff;
    --navy: #273040;
    --red: #e91f27;
    --brown-dark: #3b2a22;
    --brown-mid: #6b5048;
    --ink: #1f2a3c;
    --rule: #7a625a;
    --belt-grey: #dfe1e3;
    --ornament-tone: #ececee;
  }
  * { margin: 0; padding: 0; box-sizing: border-box; }
  html, body {
    width: 1200px; height: 925px; overflow: hidden;
    background: var(--backdrop);
  }
  .certificate {
    position: absolute; left: 56px; top: 58px;
    width: 1086px; height: 806px;
    background: var(--paper); overflow: hidden;
  }
  .side-bands { position: absolute; left: 0; top: 0; width: 280px; height: 806px; }
  .rank-ribbon { position: absolute; left: 906px; top: 0; width: 80px; height: 318px; }
  .club-seal {
    position: absolute; left: 851px; top: 84px; width: 188px; height: 188px;
    border-radius: 50%; background: var(--navy);
    border: 4px solid var(--paper); box-shadow: 0 0 0 3px var(--navy);
    display: flex; align-items: center; justify-content: center; text-align: center;
    font-family: "Cinzel", serif; font-weight: 600; font-size: 19px; line-height: 1.3;
    color: var(--paper); letter-spacing: 1px;
  }
  .belt-motif {
    position: absolute; left: 848px; top: 366px; width: 238px; height: 248px;
    background: var(--belt-grey); border-radius: 120px 0 0 120px; opacity: .85;
  }
  .programme-name {
    position: absolute; left: 300px; width: 490px; top: 96px; text-align: center;
    font-family: "Cinzel", serif; font-weight: 700; font-size: 22px;
    letter-spacing: 4px; color: var(--red);
  }
  .head-ornament {
    position: absolute; left: 444px; top: 136px; width: 200px; height: 50px;
    border-radius: 25px;
    background: radial-gradient(ellipse at center, #d9d9de 0%, var(--ornament-tone) 70%, transparent 100%);
  }
  .title-block { position: absolute; left: 300px; width: 490px; top: 0; height: 806px; }
  .title {
    position: absolute; left: 0; width: 490px; top: 204px; text-align: center;
    font-family: "Cinzel", serif; font-weight: 700; font-size: 68px;
    letter-spacing: 1px; line-height: 1; color: var(--brown-dark);
  }
  .subtitle {
    position: absolute; left: 0; width: 490px; top: 276px; text-align: center;
    font-family: "Cinzel", serif; font-weight: 600; font-size: 23px;
    letter-spacing: 1px; color: var(--brown-dark);
  }
  .subtitle-rule { position: absolute; top: 291px; height: 1.5px; width: 112px; background: var(--brown-dark); }
  .subtitle-rule.left { left: 12px; }
  .subtitle-rule.right { left: 366px; }
  .presented {
    position: absolute; left: 0; width: 1086px; top: 336px; text-align: center;
    font-family: "Cormorant Garamond", serif; font-weight: 600; font-size: 22px;
    letter-spacing: .8px; color: var(--brown-mid);
  }
  .recipient {
    position: absolute; left: 0; width: 1086px; top: 432px; text-align: center;
    font-family: "Great Vibes", cursive; font-size: 62px; color: var(--ink); line-height: 1;
  }
  .recipient-rule { position: absolute; left: 392px; top: 518px; width: 304px; height: 1.5px; background: var(--rule); }
  .rank {
    position: absolute; left: 0; width: 1086px; top: 538px; text-align: center;
    font-family: "Cormorant Garamond", serif; font-weight: 600; font-size: 19px;
    letter-spacing: .8px; color: var(--brown-mid);
  }
  .requirements {
    position: absolute; left: 270px; width: 550px; top: 564px; text-align: center;
    font-family: "Source Sans 3", sans-serif; font-size: 15.5px; line-height: 19px; color: var(--brown-mid);
  }
  .sign-line { position: absolute; top: 702px; height: 1.2px; background: var(--rule); }
  .sign-line.date { left: 248px; width: 134px; }
  .sign-line.signature { left: 670px; width: 211px; }
  .sign-label {
    position: absolute; top: 710px; text-align: center;
    font-family: "Source Sans 3", sans-serif; font-size: 15px; color: var(--ink);
  }
  .sign-label.date { left: 248px; width: 134px; }
  .sign-label.signature { left: 630px; width: 291px; }
  .instructors {
    position: absolute; left: 630px; width: 291px; top: 732px; text-align: center;
    font-family: "Source Sans 3", sans-serif; font-size: 12.5px; color: var(--brown-mid);
  }
</style>
</head>
<body>
  <main class="certificate">
    <svg class="side-bands" viewBox="0 0 280 806" aria-hidden="true">
      <polygon fill="var(--red)" points="0,0 264,0 144,380 264,806 0,806"/>
      <polygon fill="var(--navy)" points="20,0 248,0 120,306"/>
      <polygon fill="var(--paper)" points="6,0 21,0 146,384 140,384"/>
      <polygon fill="var(--navy)" points="0,358 216,806 0,806"/>
    </svg>

    <svg class="rank-ribbon" viewBox="0 0 80 318" aria-hidden="true">
      <polygon fill="var(--red)" points="0,0 80,0 80,318 40,302 0,318"/>
    </svg>
    <div class="club-seal">CORVANE<br>KICKFIST</div>

    <div class="belt-motif" role="img" aria-label="Faint illustration of a tied martial arts belt"></div>

    <p class="programme-name">IRON SASH VIGOUR</p>
    <div class="head-ornament" role="img" aria-label="Decorative calligraphic flourish"></div>

    <div class="title-block">
      <h1 class="title">CERTIFICATE</h1>
      <span class="subtitle-rule left"></span>
      <p class="subtitle">OF COMPLETION</p>
      <span class="subtitle-rule right"></span>
    </div>

    <p class="presented">THIS CERTIFICATE IS PROUDLY PRESENTED TO</p>
    <p class="recipient">Name Here</p>
    <span class="recipient-rule"></span>
    <p class="rank">WHITE BELT</p>
    <p class="requirements">10 push ups 10 Sit ups 10 squats 10 Jumping Jacks 20 sec plank 400m<br>continuous run Demonstrate beginner stretching technique</p>

    <span class="sign-line date"></span>
    <span class="sign-line signature"></span>
    <p class="sign-label date">DATE</p>
    <p class="sign-label signature">SIGNATURE</p>
    <p class="instructors">Gus Pelham &amp; Nessa Crail-Pelham</p>
  </main>
</body>
</html>
```